Unique business card design

We are looking for a design that reflects our unique social media and online marketing agency "Kestrel Media". We are a young agency with a focus on speakers, coaches and trainers. In other words, we support people who want to do good with their work and help other people live a happier, more successful and fulfilling life, reach as many people as possible with their work and thus have an influence. Our values are: sustainability, creating added value, individuality, proactivity. We want our clients to feel comfortable with us and that's why the relationship with them is very important to us. We want every customer to become a lifelong friend of the company. Most of our clients are premium coaches, meaning they are in the higher priced segment and expect seriousness, professionalism and quality. All of these things should reflect our business card as well. I look forward to feedback. Best regards, Tomas Wylander

```html
<!DOCTYPE html>
<html lang="en">
<head>
<meta charset="utf-8">
<title>Kestrel Media – Business Card</title>
<link rel="stylesheet" href="https://fonts.googleapis.com/css2?family=Michroma&family=Source+Sans+3:wght@400;600&display=swap">
<style>
  :root {
    --page: #ffffff;
    --navy: #2a2c78;
    --navy-deep: #1d1f55;
    --royal: #0f72c4;
    --ice: #c3d6e0;
    --paper: #ecebe9;
    --paper-shade: #d6d3d0;
    --white: #ffffff;
    --text-font: "Source Sans 3", "Myriad Pro", Arial, sans-serif;
    --tag-font: "Michroma", "Arial", sans-serif;
  }
  * { box-sizing: border-box; margin: 0; padding: 0; }
  html, body { width: 1200px; height: 900px; overflow: hidden; background: var(--page); }
  .canvas { position: relative; width: 1200px; height: 900px; }

  .card {
    position: absolute;
    top: 300px;
    width: 520px;
    height: 297px;
    overflow: hidden;
    box-shadow: 0 14px 28px rgba(0,0,0,0.10);
  }
  .card--front { left: 55px; }
  .card--back { left: 625px; background: var(--paper); }

  .card__art { position: absolute; inset: 0; }
  .card--front .card__art {
    background:
      linear-gradient(115deg, var(--ice) 0 9%, transparent 9%),
      linear-gradient(140deg, var(--navy) 0%, var(--navy-deep) 35%, var(--royal) 62%, var(--navy) 100%);
  }
  .card--back .card__art {
    background: linear-gradient(120deg, var(--paper) 0%, var(--paper) 40%, var(--paper-shade) 70%, #e4e2df 100%);
  }

  .brand { position: absolute; }
  .brand__row { display: flex; align-items: center; gap: 10px; }
  .brand__square { flex: none; }
  .brand__name {
    font-family: var(--text-font);
    font-weight: 600;
    line-height: 1;
    white-space: nowrap;
  }
  .brand__tagline {
    font-family: var(--tag-font);
    white-space: nowrap;
    margin-top: 6px;
  }

  .card--front .brand { left: 258px; top: 176px; }
  .card--front .brand__square { width: 22px; height: 22px; background: var(--white); }
  .card--front .brand__name { font-size: 36px; color: var(--white); }
  .card--front .brand__tagline { font-size: 9.5px; color: var(--white); padding-left: 32px; }

  .card--back .brand { left: 40px; top: 34px; }
  .card--back .brand__square { width: 40px; height: 40px; background: var(--navy); }
  .card--back .brand__name { font-size: 32px; color: var(--navy); }
  .card--back .brand__tagline { font-size: 8.5px; color: var(--navy); }

  .contacts {
    position: absolute;
    left: 40px;
    top: 150px;
    list-style: none;
    font-family: var(--text-font);
    font-size: 13px;
    color: var(--navy);
  }
  .contacts__item { display: flex; align-items: center; gap: 6px; height: 17px; }
  .contacts__item--gap { margin-top: 8px; }
  .contacts__icon { width: 13px; height: 13px; flex: none; fill: var(--navy); }
</style>
</head>
<body>
<main class="canvas">

  <section class="card card--front" aria-label="Card front">
    <div class="card__art" role="img" aria-label="Abstract overlapping blue and navy geometric shapes"></div>
    <div class="brand">
      <div class="brand__row">
        <span class="brand__square"></span>
        <span class="brand__name">Kestrel Media</span>
      </div>
      <p class="brand__tagline">Online Marketing Services</p>
    </div>
  </section>

  <section class="card card--back" aria-label="Card back">
    <div class="card__art" role="img" aria-label="Faint grey overlapping geometric shapes"></div>
    <div class="brand">
      <div class="brand__row">
        <span class="brand__square"></span>
        <span class="brand__name">Kestrel Media</span>
      </div>
      <p class="brand__tagline">Online Marketing Services</p>
    </div>

    <ul class="contacts">
      <li class="contacts__item">
        <svg class="contacts__icon" viewBox="0 0 16 16" aria-hidden="true"><path d="M3 1l3 3-1.5 2c1 2 3 4 5 5L11.5 9.5l3 3-2 2.5C7 14 2 9 1 3z"/></svg>
        555.310.0800
      </li>
      <li class="contacts__item">
        <svg class="contacts__icon" viewBox="0 0 16 16" aria-hidden="true"><rect x="1" y="6" width="14" height="8" rx="1"/><rect x="4" y="1" width="8" height="6" fill="none" stroke="currentColor"/><rect x="4" y="1" width="8" height="4"/></svg>
        555.310.0900
      </li>
      <li class="contacts__item">
        <svg class="contacts__icon" viewBox="0 0 16 16" aria-hidden="true"><rect x="4" y="0" width="8" height="16" rx="1.5"/><rect x="5.5" y="2" width="5" height="9" fill="#ecebe9"/></svg>
        555.318.4621
      </li>
      <li class="contacts__item contacts__item--gap">
        <svg class="contacts__icon" viewBox="0 0 16 16" aria-hidden="true"><rect x="1" y="3" width="14" height="10" rx="1"/><path d="M1.5 4l6.5 5 6.5-5" fill="none" stroke="#ecebe9" stroke-width="1.4"/></svg>
        info@kestrelmedia.com
      </li>
      <li class="contacts__item">
        <svg class="contacts__icon" viewBox="0 0 16 16" aria-hidden="true"><circle cx="8" cy="8" r="7"/><path d="M1 8h14M8 1v14M8 1c-3 3-3 11 0 14M8 1c3 3 3 11 0 14" fill="none" stroke="#ecebe9" stroke-width="0.9"/></svg>
        www.kestrelmedia.com
      </li>
      <li class="contacts__item contacts__item--gap">
        <svg class="contacts__icon" viewBox="0 0 16 16" aria-hidden="true"><path d="M8 1l7 7h-2v7H9.5v-4.5h-3V15H3V8H1z"/></svg>
        2240 Harlow Street, Brookfield, SC 29680
      </li>
    </ul>
  </section>

</main>
</body>
</html>
```